A Dedicated Thank You to my Dad

Proposed Dimensions: Approx. 20" x 30"

For Father's Day, I wrote a dedication to my Dad that encapsulates my gratitude for everything he does, and everything he is. His birthday is on August 3, but it is more important for me to transform this dedication into a meaningful and memorable gift than to meet any deadline. I would love an image that captures the relationship between a father and his son, accompanied by my words of thanks in some sort of font that is appropriate for the message (calligprahy? not sure about that).

I had actually posted the Thank You on Chatterloop as a public post, so anyone with an account can read it: https://www.chatterloop.example/photo.php?fbid=20473819265038417&set=a.918364027159.5829361.3940582&type=1&theater

Only the words starting with "Thank you ..." should be on the poster.

Target Market(s)

This is a personal gift for my Dad. He doesn't have the best of eyesight, so having the words in a really small font would not be particularly helpful. :-)

Requirements
Must have
• * Personable
* Warm
* Inviting
* Memorable
* Understated more favored over Loud
Should not have
• * An entire palette of colors
* Wacky colors or fonts

```html
<!DOCTYPE html>
<html lang="en">
<head>
<meta charset="utf-8">
<title>A Dedicated Thank You</title>
<link rel="stylesheet" href="https://fonts.googleapis.com/css2?family=Allura&family=Mrs+Saint+Delafield&family=Open+Sans:wght@700&display=swap">
<style>
  :root {
    --backdrop: #000000;
    --paper: #ffffff;
    --ink: #1f1f1f;
    --accent-plum: #8b2a7f;
    --sky: #7cc3ea;
    --rule: #a9d6f0;
  }
  * { margin: 0; padding: 0; box-sizing: border-box; }
  html, body {
    width: 1200px; height: 1000px; overflow: hidden;
    background: var(--backdrop);
  }
  .poster {
    position: absolute; left: 101px; top: 168px;
    width: 998px; height: 664px;
    background: var(--paper);
    overflow: hidden;
  }
  .portrait {
    position: absolute; left: 470px; top: 50px;
    width: 530px; height: 480px;
    background:
      radial-gradient(ellipse 90px 80px at 175px 90px, rgba(120,200,120,.75), transparent 70%),
      radial-gradient(ellipse 130px 110px at 290px 80px, rgba(250,190,60,.8), transparent 70%),
      radial-gradient(ellipse 110px 120px at 190px 230px, rgba(240,110,150,.7), transparent 70%),
      radial-gradient(ellipse 150px 150px at 300px 260px, rgba(245,200,150,.75), transparent 72%),
      radial-gradient(ellipse 140px 110px at 170px 380px, rgba(120,200,200,.6), transparent 70%),
      radial-gradient(ellipse 200px 120px at 430px 390px, rgba(245,140,90,.6), transparent 70%);
  }
  .title {
    position: absolute; left: 4px; top: 14px;
    font-family: "Allura", cursive;
    font-weight: 400; font-synthesis: none;
    font-size: 112px; line-height: 1.1; color: var(--sky);
    white-space: nowrap;
  }
  .rules { position: absolute; left: 0; top: 0; }
  .note {
    position: absolute;
    font-family: "Open Sans", sans-serif; font-weight: 700;
    font-size: 12.8px; line-height: 14.6px;
    color: var(--ink); white-space: nowrap;
  }
  .note--right { text-align: right; }
  .note em { font-style: normal; color: var(--accent-plum); }
  .closing {
    position: absolute;
    font-family: "Mrs Saint Delafield", cursive;
    font-weight: 400; font-synthesis: none;
    font-size: 28px; line-height: 1.2; color: var(--ink);
    white-space: nowrap;
  }
  .closing--accent { color: var(--accent-plum); }
</style>
</head>
<body>
<main class="poster">
  <div class="portrait" role="img" aria-label="Portrait photograph of the father in soft multicolour tint, fading into white"></div>

  <svg class="rules" width="998" height="664" aria-hidden="true">
    <g stroke="var(--rule)" stroke-width="1">
      <line x1="47" y1="104" x2="47" y2="278"/>
      <line x1="237" y1="108" x2="237" y2="232"/>
      <line x1="237" y1="244" x2="237" y2="334"/>
      <line x1="281" y1="168" x2="281" y2="366"/>
      <line x1="281" y1="390" x2="281" y2="497"/>
      <line x1="324" y1="130" x2="324" y2="272"/>
      <line x1="309" y1="390" x2="309" y2="497"/>
      <line x1="369" y1="102" x2="369" y2="176"/>
      <line x1="47" y1="436" x2="47" y2="574"/>
    </g>
  </svg>

  <h1 class="title">Thank you</h1>

  <p class="note note--right" style="right:770px; top:170px;">Thank you for<br>welcoming more people<br>to stay with us than<br><em>I can count.</em></p>
  <p class="note note--right" style="right:770px; top:278px;">Thank you for<br>my dry sense<br>of humor.<br><em>I cherish it.</em></p>
  <p class="note" style="left:56px; top:364px;">Thank you for never giving up<br>on trying to convince<br>me that imperfection is<br><em>not a failure.</em></p>
  <p class="note note--right" style="right:727px; top:439px;">Thank you for<br>showing me that there<br>is peace to be found in<br><em>stillness and quiet.</em></p>
  <p class="note" style="left:56px; top:524px;">Thank you for<br>trusting me enough<br>to let your guard down<br>to let me know how<br><em>you are truly doing.</em></p>

  <p class="note" style="left:377px; top:119px;">Thank you for<br>teaching me<br>to try to find the<br><em>good in everyone.</em></p>
  <p class="note" style="left:333px; top:201px;">Thank you for<br>demonstrating the<br>fun that can be had<br>and the truths that can<br><em>be gleaned from debate.</em></p>
  <p class="note" style="left:290px; top:294px;">Thank you for<br>doing whatever you<br>can to help whoever<br>you can, <em>whether friend,<br>family or stranger.</em></p>
  <p class="note" style="left:333px; top:410px;">Thank you for<br>accepting me for<br>who I am, no matter<br>who I love, and for<br><em>helping me to<br>accept myself.</em></p>

  <p class="closing" style="left:368px; top:526px;">Thank you for insisting, year after year,</p>
  <p class="closing" style="left:336px; top:556px;">that time with you means more than any gift I</p>
  <p class="closing" style="left:442px; top:586px;">could ever purchase. That is one lesson, amongst so many,</p>
  <p class="closing closing--accent" style="left:428px; top:616px;">that I will pass down to our next generation.</p>
</main>
</body>
</html>
```